Postcard Design Seabright Mews

I need a postcard design to publicise my holiday let in Falmouth. The postcard needs to refer to the location which is 27 Seabright Mews Falmouth and include on the front For bookings or further information visit TWRetreats www.twretreats.co.ukor telephone 01872 938204.The postcard needs to be small size, glossy on one side and conventional on the reverse.The following documents are relevant picture of building and local photo.

```html
<!DOCTYPE html>
<html lang="en">
<head>
<meta charset="utf-8">
<title>Seabright Mews Postcard</title>
<link rel="stylesheet" href="https://fonts.googleapis.com/css2?family=Roboto+Condensed:wght@400;700&family=Lato:wght@400;700;900&display=swap">
<style>
  :root {
    --page-bg: #e9e9e9;
    --card-white: #ffffff;
    --orange: #e8a021;
    --orange-deep: #d98a12;
    --orange-soft: rgba(240, 170, 50, 0.72);
    --blue: #1f4f9c;
    --ink: #333333;
    --ink-dark: #222222;
    --grey-light: #d6d6d6;
    --grey-mid: #a9a9a9;
    --grey-dark: #7a7a7a;
    --harbour-top: #c9c6c1;
    --harbour-bottom: #6f6a63;
  }
  * { box-sizing: border-box; margin: 0; padding: 0; }
  html, body {
    width: 804px; height: 1200px; overflow: hidden;
    background: var(--page-bg);
  }
  .postcard {
    position: absolute; left: 32px; width: 740px; height: 520px;
    background: var(--card-white);
    overflow: hidden;
    box-shadow: 0 2px 6px rgba(0,0,0,0.18);
  }
  .postcard--front { top: 40px; }
  .postcard--back { top: 630px; }
  .postcard svg.shapes { position: absolute; inset: 0; }

  /* front */
  .title {
    position: absolute; left: 52px; top: 34px; width: 308px; text-align: center;
    font-family: "Roboto Condensed", sans-serif;
  }
  .title__line1 { display: block; color: var(--blue); font-weight: 700; font-size: 44px; line-height: 1; letter-spacing: 0.5px; }
  .title__line2 { display: block; color: var(--ink-dark); font-weight: 700; font-size: 27px; line-height: 1.2; margin-top: 4px; }
  .brand {
    position: absolute; right: 40px; top: 48px;
    display: flex; align-items: center; gap: 10px;
    font-family: "Lato", sans-serif; font-weight: 900; font-size: 30px; color: var(--blue);
  }
  .brand__dot { width: 18px; height: 18px; border-radius: 50%; background: var(--orange); }
  .call {
    position: absolute; right: 24px; top: 318px; text-align: right;
    font-family: "Roboto Condensed", sans-serif; font-weight: 700;
  }
  .call__label { display: block; color: var(--card-white); font-size: 32px; line-height: 1; }
  .call__number { display: block; color: var(--ink-dark); font-size: 42px; line-height: 1.1; margin-top: 2px; }
  .booking {
    position: absolute; right: 24px; top: 440px; width: 330px; text-align: center;
    font-family: "Lato", sans-serif;
  }
  .booking__label {
    display: block; color: var(--blue); font-weight: 700; font-size: 19px;
    padding-bottom: 6px; border-bottom: 2px solid var(--blue);
  }
  .booking__url { display: block; color: var(--ink); font-weight: 700; font-size: 25px; margin-top: 6px; letter-spacing: 0.5px; }

  /* back */
  .description {
    position: absolute; left: 30px; top: 168px; width: 400px;
    font-family: "Lato", sans-serif; font-size: 14.5px; line-height: 1.4; color: var(--ink-dark);
  }
  .facts {
    position: absolute; left: 30px; top: 280px; width: 390px;
    display: grid; grid-template-columns: 200px 190px; row-gap: 20px;
    list-style: none;
    font-family: "Lato", sans-serif; font-weight: 700; font-size: 14.5px; color: var(--ink-dark);
  }
  .facts li { display: flex; align-items: center; gap: 14px; }
  .facts li::before { content: ""; width: 8px; height: 8px; border-radius: 50%; background: var(--card-white); }
  .back-url {
    position: absolute; left: 54px; top: 466px;
    font-family: "Lato", sans-serif; font-weight: 700; font-size: 22px; letter-spacing: 1px; color: var(--card-white);
  }
  .stamp-box {
    position: absolute; left: 636px; top: 66px; width: 72px; height: 84px;
    border: 1px solid #9a9a9a;
  }
  .address-line {
    position: absolute; left: 510px; width: 196px; height: 0;
    border-top: 2px solid var(--ink-dark);
  }
</style>
</head>
<body>

<section class="postcard postcard--front" aria-label="Postcard front">
  <svg class="shapes" width="740" height="520" viewBox="0 0 740 520">
    <defs>
      <linearGradient id="harbourTone" x1="0" y1="0" x2="0" y2="1">
        <stop offset="0" stop-color="var(--harbour-top)"/>
        <stop offset="1" stop-color="var(--harbour-bottom)"/>
      </linearGradient>
      <linearGradient id="buildingTone" x1="0" y1="0" x2="0" y2="1">
        <stop offset="0" stop-color="#7fa7d6"/>
        <stop offset="0.55" stop-color="#e9ecef"/>
        <stop offset="1" stop-color="#6f7d5e"/>
      </linearGradient>
    </defs>
    <rect class="harbour-photo" role="img" aria-label="Photo of Falmouth harbour with moored boats and the marina" x="0" y="0" width="740" height="440" fill="url(#harbourTone)"/>
    <rect class="title-panel" x="52" y="0" width="308" height="430" fill="var(--orange-soft)"/>
    <path class="front-wave-line" d="M0,412 C220,420 430,290 740,250" fill="none" stroke="var(--card-white)" stroke-width="6"/>
    <path class="front-wave" d="M0,420 C220,428 430,298 740,262 L740,520 L0,520 Z" fill="var(--orange)"/>
    <path class="front-white-band" d="M250,520 C275,468 320,440 400,434 L740,430 L740,520 Z" fill="var(--card-white)"/>
    <circle class="building-photo" role="img" aria-label="Photo of the white three-storey apartment building" cx="200" cy="345" r="112" fill="url(#buildingTone)" stroke="var(--card-white)" stroke-width="8"/>
  </svg>

  <h1 class="title">
    <span class="title__line1">27 SEABRIGHT</span>
    <span class="title__line2">MEWS FALMOUTH</span>
  </h1>
  <div class="brand"><span class="brand__dot"></span>TWRetreats</div>
  <p class="call">
    <span class="call__label">CALL NOW</span>
    <span class="call__number">01872 938204</span>
  </p>
  <p class="booking">
    <span class="booking__label">FOR BOOKINGS VISIT TODAY</span>
    <span class="booking__url">www.twretreats.co.uk</span>
  </p>
</section>

<section class="postcard postcard--back" aria-label="Postcard reverse">
  <svg class="shapes" width="740" height="520" viewBox="0 0 740 520">
    <defs>
      <linearGradient id="panelTone" x1="0" y1="0" x2="1" y2="0">
        <stop offset="0" stop-color="#bdbdbd"/>
        <stop offset="0.6" stop-color="#d4d4d4"/>
        <stop offset="1" stop-color="#9c9c9c"/>
      </linearGradient>
      <linearGradient id="roomTone" x1="0" y1="0" x2="0" y2="1">
        <stop offset="0" stop-color="#8a8a8a"/>
        <stop offset="1" stop-color="#dcdcdc"/>
      </linearGradient>
    </defs>
    <path class="info-panel" d="M0,0 L360,0 C420,60 440,200 430,300 C425,390 420,450 440,520 L0,520 Z" fill="url(#panelTone)"/>
    <path class="lounge-photo" role="img" aria-label="Photo of the lounge with sofas and a coffee table" d="M0,0 L330,0 C350,40 350,100 320,122 C250,140 140,150 0,128 Z" fill="url(#roomTone)"/>
    <path class="photo-edge" d="M0,132 C140,154 255,144 324,126" fill="none" stroke="var(--card-white)" stroke-width="6"/>
    <path class="bay-photo" role="img" aria-label="Photo of the sitting room with a bay window and armchairs" d="M0,400 C120,372 300,370 390,385 C420,420 420,480 415,520 L0,520 Z" fill="url(#roomTone)"/>
    <path class="photo-edge" d="M0,394 C120,366 300,364 394,380" fill="none" stroke="var(--card-white)" stroke-width="6"/>
  </svg>

  <p class="description">This beautifully presented, first floor apartment is situated in a quiet area of Falmouth yet only a couple of minutes walk to the Harbourside Marina and the town centre and walking distance to the stunning Gullcove Beach. WIFI included.</p>
  <ul class="facts">
    <li>SLEEPS: 4</li>
    <li>PETS: NO</li>
    <li>TARIFF BAND: L</li>
    <li>BEDROOMS: 2</li>
  </ul>
  <p class="back-url">www.twretreats.co.uk</p>

  <div class="stamp-box"></div>
  <div class="address-line" style="top:276px"></div>
  <div class="address-line" style="top:312px"></div>
  <div class="address-line" style="top:348px"></div>
</section>

</body>
</html>
```